Classic/Royal 5 Items Black coloured Stationery Design

Hello,
I'm looking for an Elegant Stationery set consists of 5 items as the following,
1- Letterhead
2- Business Card
3- Invoice
4- CD/DVD with their Envelope Design
5- Envelope
To let the project move ahead easily, I've included a folder consists many designs I liked from various design sites and it consists of,
1- Business card
2- Corporate Identity
3- Invoice
4- Miscellanies
Inside the first three folders, you will find a folder named "Recommended", it contains designs that I like so much and hoping to have a design like them.
The "Miscellanies" folder got some designs for Inspiration.
I'm waiting for some greats designs, a joomla template designer is a bonus for me as I will need him to design the website layer soon.
Due to upload problems at ArtHarbor, I've uploaded the folder in a .rar archive at multiple site and here is the link http://filevanta.example/QZTRLPNB .
Thank you
Update :- You can use this alternative download link from my Nimbox drive to download the designs
https://share.cloudvessel.example/file/d/7Hq2pLx9w4t6KmZr83VnbYsQ5eJd
Business

```html
<!DOCTYPE html>
<html lang="en">
<head>
<meta charset="utf-8">
<title>Vale Crest — Business Card</title>
<link rel="stylesheet" href="https://fonts.googleapis.com/css2?family=Playfair+Display:wght@400;600&family=Poppins:wght@400&display=swap">
<style>
  :root {
    --backdrop: #2b2622;
    --card-dark: #141414;
    --card-mid: #2a2a2a;
    --silver: #c9c9c9;
    --silver-soft: #a8a8a8;
    --mark-fill: #0c0c0c;
    --mark-frame: #d6d6d6;
  }
  html, body {
    margin: 0;
    width: 1200px;
    height: 788px;
    overflow: hidden;
    background: var(--backdrop);
  }
  .stage {
    position: relative;
    width: 1200px;
    height: 788px;
  }
  .card {
    position: absolute;
    top: 251px;
    width: 500px;
    height: 286px;
    border-radius: 3px;
    overflow: hidden;
    box-shadow: 0 10px 28px rgba(0,0,0,0.45);
    color: var(--silver);
    text-align: center;
  }
  .card--contact { left: 60px; }
  .card--brand { left: 640px; }
  .card__texture {
    position: absolute;
    inset: 0;
    background: radial-gradient(ellipse at 50% 40%, var(--card-mid) 0%, var(--card-dark) 75%);
  }
  .card__corner {
    position: absolute;
    width: 18px;
    height: 18px;
    background: #3a3a3a;
  }
  .card__corner--tl { top: 10px; left: 10px; }
  .card__corner--tr { top: 10px; right: 10px; }
  .card__corner--bl { bottom: 10px; left: 10px; }
  .card__corner--br { bottom: 10px; right: 10px; }
  .card__content {
    position: relative;
    display: flex;
    flex-direction: column;
    align-items: center;
  }
  .brand-square {
    background: var(--mark-fill);
    border: 2px solid var(--mark-frame);
    outline: 1px solid var(--mark-fill);
  }
  .brand-name {
    font-family: "Playfair Display", serif;
    font-weight: 600;
    color: var(--silver);
    line-height: 1;
  }
  .brand-tagline {
    font-family: "Poppins", sans-serif;
    font-weight: 400;
    color: var(--silver-soft);
    line-height: 1;
  }
  /* contact side */
  .card--contact .card__content { padding-top: 20px; }
  .card--contact .brand-square { width: 42px; height: 42px; }
  .card--contact .brand-name { font-size: 24px; margin-top: 8px; }
  .card--contact .brand-tagline { font-size: 10px; margin-top: 4px; }
  .person-name {
    font-family: "Playfair Display", serif;
    font-size: 15px;
    letter-spacing: 2px;
    text-transform: uppercase;
    margin-top: 12px;
    color: var(--silver);
  }
  .contact-list {
    list-style: none;
    margin: 16px 0 0;
    padding: 0;
    font-family: "Playfair Display", serif;
    font-size: 12px;
    line-height: 17px;
    color: var(--silver);
  }
  /* brand side */
  .card--brand .card__content { padding-top: 62px; }
  .card--brand .brand-square { width: 64px; height: 64px; }
  .card--brand .brand-name { font-size: 38px; margin-top: 12px; }
  .card--brand .brand-tagline { font-size: 14px; margin-top: 6px; }
</style>
</head>
<body>
<main class="stage">

  <section class="card card--contact" aria-label="Business card, contact side">
    <div class="card__texture" role="img" aria-label="Dark damask pattern background"></div>
    <div class="card__corner card__corner--tl" role="img" aria-label="Corner ornament"></div>
    <div class="card__corner card__corner--tr" role="img" aria-label="Corner ornament"></div>
    <div class="card__corner card__corner--bl" role="img" aria-label="Corner ornament"></div>
    <div class="card__corner card__corner--br" role="img" aria-label="Corner ornament"></div>
    <div class="card__content">
      <div class="brand-square"></div>
      <div class="brand-name">Vale Crest</div>
      <div class="brand-tagline">Hotels and General Supplies</div>
      <div class="person-name">Daniel R. Hart</div>
      <ul class="contact-list">
        <li>(123) 555 0148</li>
        <li>danielhart@valecrest.example</li>
        <li>www.valecrest.example</li>
      </ul>
    </div>
  </section>

  <section class="card card--brand" aria-label="Business card, brand side">
    <div class="card__texture" role="img" aria-label="Dark damask pattern background"></div>
    <div class="card__content">
      <div class="brand-square"></div>
      <div class="brand-name">Vale Crest</div>
      <div class="brand-tagline">Hotels and General Supplies</div>
    </div>
  </section>

</main>
</body>
</html>
```